Email Advertisement - Designed for airplane buyers to review an airplane.

We need an email ad template to feature an airplane for sale. It should be a clean white type design with no photo shop done inside the photos. It should also be able to be built as a responsive design.

Target Market(s)

Sent to potential aircraft buyers

Industry/Entity Type

Shop

Font styles to use
Sans Serif

Colors
34a6d7
85cae6
ffffff

Requirements
Must have
• Some of the photos may link to a video tour, the website or an email

```html
<!DOCTYPE html>
<html lang="en">
<head>
<meta charset="utf-8">
<title>SkyVela – Aircraft Listing Email</title>
<link href="https://fonts.googleapis.com/css2?family=Roboto:wght@400;500&family=Questrial&display=swap" rel="stylesheet">
<style>
:root{
  --page-bg:#dcdcdc;
  --band:#b9cbe0;
  --accent:#34a6d7;
  --accent-light:#85cae6;
  --white:#ffffff;
  --ink:#3c3c3c;
  --ink-soft:#555;
  --line:#e2e2e2;
  --tick:#b5b5b5;
}
*{margin:0;padding:0;box-sizing:border-box}
html,body{width:1200px;height:2429px;overflow:hidden;background:var(--page-bg)}
body{position:relative;font-family:"Roboto",sans-serif;color:var(--ink)}
.pre-header{position:absolute;top:92px;left:0;width:1200px;text-align:center;font-family:"Questrial",sans-serif;font-size:20px;color:#222;letter-spacing:.4px}
.pre-header a{color:#222}
.email{position:absolute;left:193px;top:154px;width:814px;height:2088px;background:var(--white);box-shadow:0 14px 18px -10px rgba(0,0,0,.18)}
.hero{position:absolute;left:0;top:0;width:814px;height:656px;background:linear-gradient(180deg,var(--band) 0%,var(--band) 45%,#dfe7f1 70%,var(--white) 100%)}
.brand{position:absolute;left:0;width:814px;text-align:center;font-family:"Roboto",sans-serif;font-weight:400;color:#3b3f48;letter-spacing:3px}
.hero .brand{top:68px;font-size:56px}
.social-outline{position:absolute;top:16px;right:36px;display:flex;gap:6px}
.social-outline span{width:38px;height:38px;border:2px solid var(--white);border-radius:50%}
.hero-art{position:absolute;left:220px;top:194px;width:397px;height:194px;border-radius:12px;background:linear-gradient(160deg,#8fa9cc 0%,#dfe6f0 55%,#a9b9d0 100%)}
.hero-title{position:absolute;top:584px;left:0;width:814px;text-align:center;font-size:26px;color:var(--ink)}
.listing-icon{position:absolute;left:387px;top:708px}
.listing-title{position:absolute;top:752px;left:0;width:814px;text-align:center;font-size:25px;color:var(--accent);letter-spacing:.5px}
.listing-rule{position:absolute;left:379px;top:796px;width:56px;height:1px;background:#cfcfcf}
.photo{position:absolute;border-radius:50%}
.photo-cockpit{left:32px;top:958px;width:188px;height:188px;background:radial-gradient(circle,#6b7886,#2d3440)}
.photo-exterior{left:246px;top:873px;width:320px;height:320px;background:linear-gradient(180deg,#8faebf 0%,#a9bfc9 50%,#5f7a4e 75%,#466a3c 100%)}
.photo-cabin{left:589px;top:944px;width:188px;height:188px;background:radial-gradient(circle,#e6d5bf,#8a6b4c)}
.badge{position:absolute;width:80px;height:80px;border-radius:50%;background:var(--accent);display:flex;align-items:center;justify-content:center}
.badge-engine{left:84px;top:1090px}
.badge-plane{left:368px;top:1150px}
.badge-seat{left:649px;top:1090px}
.specs{position:absolute;left:89px;top:1280px;width:636px;height:449px;border:1px solid var(--line)}
.spec-list{list-style:none;position:absolute;left:136px;top:62px}
.spec-list li{display:flex;align-items:center;height:45px;font-size:17px}
.spec-list svg{margin-right:11px}
.spec-label{width:181px;font-weight:500;color:#333}
.spec-value{color:var(--ink-soft)}
.enquire{position:absolute;left:210px;top:358px;width:172px;height:49px;border:2px solid #9a9a9a;display:flex;align-items:center;justify-content:center;font-family:"Questrial",sans-serif;font-size:19px;color:#333;letter-spacing:1px}
.footer{position:absolute;left:0;top:1795px;width:814px;height:293px;background:var(--band)}
.footer .brand{top:52px;font-size:44px}
.social-solid{position:absolute;top:141px;left:0;width:814px;display:flex;justify-content:center;gap:22px}
.social-solid span{width:39px;height:39px}
.social-solid .s1{background:#3b5998}
.social-solid .s2{background:#35a8e0}
.social-solid .s3{background:#d44a4a}
.contact{position:absolute;top:198px;left:0;width:814px;text-align:center;font-family:"Questrial",sans-serif;font-size:18px;line-height:31px;color:#444;letter-spacing:.5px}
</style>
</head>
<body>
<p class="pre-header">For anything about this mail you can contract us by <a href="#">click this link.</a></p>

<main class="email">
  <header class="hero">
    <div class="social-outline"><span></span><span></span><span></span></div>
    <div class="brand">SKYVELA</div>
    <div class="hero-art" role="img" aria-label="Illustration of a jet airliner flying over a faint world map"></div>
    <h1 class="hero-title" style="font-weight:400">Wellcome to Airoplane Buying</h1>
  </header>

  <svg class="listing-icon" width="40" height="32" viewBox="0 0 40 32" fill="none" stroke="#b0b0b0" stroke-width="1.5" stroke-linejoin="round">
    <path d="M2 16h34c2 0 3-1 3-1s-1-1-3-1H24L14 3h-4l6 11H8L5 9H2l2 7-2 7h3l3-5h8l-6 11h4l10-11"/>
  </svg>
  <h2 class="listing-title" style="font-weight:400">1975 CORVANE CX 50</h2>
  <div class="listing-rule"></div>

  <div class="photo photo-cockpit" role="img" aria-label="Photo of the aircraft cockpit instrument panel"></div>
  <div class="photo photo-exterior" role="img" aria-label="Photo of the business jet in flight above farmland"></div>
  <div class="photo photo-cabin" role="img" aria-label="Photo of the cream leather cabin interior"></div>

  <a class="badge badge-engine" href="#" aria-label="Engine details">
    <svg width="40" height="30" viewBox="0 0 40 30" fill="none" stroke="#fff" stroke-width="2" stroke-linejoin="round">
      <path d="M9 7h14v4h6v4h4v-4h4v12h-4v-4h-4v5H13l-4-4H6v4H3V10h3v4h3z"/><path d="M20 12l-4 6h5l-3 5"/>
    </svg>
  </a>
  <a class="badge badge-plane" href="#" aria-label="Video tour">
    <svg width="36" height="36" viewBox="0 0 36 36" fill="none" stroke="#fff" stroke-width="2" stroke-linejoin="round">
      <path d="M30 6c-2-2-5 0-7 2l-5 5-11-3-3 3 9 5-4 5-4-1-2 2 5 3 3 5 2-2-1-4 5-4 5 9 3-3-3-11 5-5c2-2 4-5 2-7z"/>
    </svg>
  </a>
  <a class="badge badge-seat" href="#" aria-label="Cabin interior">
    <svg width="38" height="32" viewBox="0 0 38 32" fill="none" stroke="#fff" stroke-width="2" stroke-linejoin="round">
      <path d="M8 14V8c0-3 2-5 5-5h12c3 0 5 2 5 5v6"/><path d="M4 14c2-2 5-1 5 2v4h20v-4c0-3 3-4 5-2s1 4 0 5v7H4v-7c-1-1-2-3 0-5z"/><path d="M8 26v3M30 26v3"/>
    </svg>
  </a>

  <section class="specs">
    <ul class="spec-list">
      <li><svg width="22" height="22" viewBox="0 0 22 22"><circle cx="11" cy="11" r="11" fill="var(--tick)"/><path d="M6 11l3.5 3.5L16 8" stroke="#fff" stroke-width="2.2" fill="none"/></svg><span class="spec-label">Sale Status:</span><span class="spec-value">For Sale</span></li>
      <li><svg width="22" height="22" viewBox="0 0 22 22"><circle cx="11" cy="11" r="11" fill="var(--tick)"/><path d="M6 11l3.5 3.5L16 8" stroke="#fff" stroke-width="2.2" fill="none"/></svg><span class="spec-label">Year:</span><span class="spec-value">2017</span></li>
      <li><svg width="22" height="22" viewBox="0 0 22 22"><circle cx="11" cy="11" r="11" fill="var(--tick)"/><path d="M6 11l3.5 3.5L16 8" stroke="#fff" stroke-width="2.2" fill="none"/></svg><span class="spec-label">Make/Model:</span><span class="spec-value">NORVALE AIRCRAFT RIDGE</span></li>
      <li><svg width="22" height="22" viewBox="0 0 22 22"><circle cx="11" cy="11" r="11" fill="var(--tick)"/><path d="M6 11l3.5 3.5L16 8" stroke="#fff" stroke-width="2.2" fill="none"/></svg><span class="spec-label">Registration #:</span><span class="spec-value">N718KV</span></li>
      <li><svg width="22" height="22" viewBox="0 0 22 22"><circle cx="11" cy="11" r="11" fill="var(--tick)"/><path d="M6 11l3.5 3.5L16 8" stroke="#fff" stroke-width="2.2" fill="none"/></svg><span class="spec-label">Serial #:</span><span class="spec-value">200-0416</span></li>
      <li><svg width="22" height="22" viewBox="0 0 22 22"><circle cx="11" cy="11" r="11" fill="var(--tick)"/><path d="M6 11l3.5 3.5L16 8" stroke="#fff" stroke-width="2.2" fill="none"/></svg><span class="spec-label">Location</span><span class="spec-value">Harlow Field, USA</span></li>
    </ul>
    <a class="enquire" href="#">Enquire Now</a>
  </section>

  <footer class="footer">
    <div class="brand">SKYVELA</div>
    <div class="social-solid"><span class="s1"></span><span class="s2"></span><span class="s3"></span></div>
    <p class="contact">Phone: + 000 4 555 01 23 | Mobile: + 000 55 01 24 678<br>E-mail: sales@skyvela.example | Web: www.skyvela.example</p>
  </footer>
</main>
</body>
</html>
```